New Signage Design Project

Real estate company looking for signage, PowerPoint and stationery branding. Signs will be placed in front of homes and other properties being sold

Name of company is Birch Crest, LLC

Requirements
Must have
• Name of company - Birch Crest, LLC

```html
<!DOCTYPE html>
<html lang="en">
<head>
<meta charset="utf-8">
<title>Birch Crest, LLC – For Sale Yard Sign</title>
<link rel="stylesheet" href="https://fonts.googleapis.com/css2?family=Roboto+Condensed:wght@300;700&family=Roboto:wght@500&display=swap">
<style>
  :root {
    --stage: #d4d4d4;
    --sign-top: #2c3a3c;
    --sign-bottom: #20292a;
    --photo-top: #34474a;
    --photo-bottom: #232e2f;
    --accent-red: #e34f5c;
    --sage: #7f9f9c;
    --sage-light: #8eaeaa;
    --sage-edge: #b4d6d1;
    --ink: #222c2d;
    --white: #ffffff;
    --web: #8cb1ad;
  }
  * { margin: 0; padding: 0; box-sizing: border-box; }
  html, body {
    width: 1200px;
    height: 1200px;
    overflow: hidden;
    background: var(--stage);
  }
  .yard-sign {
    position: absolute;
    left: 220px;
    top: 30px;
    width: 760px;
    height: 1140px;
    background: var(--sign-bottom);
    overflow: hidden;
  }
  .house-photo {
    position: absolute;
    left: 0;
    top: 0;
    width: 760px;
    height: 810px;
    background: linear-gradient(180deg, var(--sign-top) 0%, var(--photo-top) 45%, var(--photo-bottom) 100%);
  }
  .headline {
    position: absolute;
    left: 0;
    top: 30px;
    width: 760px;
    text-align: center;
    font-family: "Roboto Condensed", "Arial Narrow", sans-serif;
    font-weight: 700;
    font-size: 162px;
    line-height: 1;
    letter-spacing: 1px;
    color: var(--accent-red);
  }
  .brand {
    position: absolute;
    left: 0;
    top: 400px;
    width: 760px;
    display: flex;
    align-items: center;
    justify-content: center;
    gap: 26px;
  }
  .brand-dot {
    width: 78px;
    height: 78px;
    border-radius: 50%;
    background: var(--accent-red);
  }
  .brand-name {
    font-family: "Roboto Condensed", "Arial Narrow", sans-serif;
    font-weight: 700;
    font-size: 78px;
    line-height: 1;
    color: var(--white);
  }
  .phone-bar {
    position: absolute;
    left: 51px;
    top: 749px;
    width: 658px;
    height: 111px;
    border: 2px solid var(--sage-edge);
    border-radius: 16px;
    background: linear-gradient(90deg, var(--sage) 0%, var(--sage-light) 50%, var(--sage) 100%);
    box-shadow: 0 22px 20px -14px rgba(0,0,0,0.7);
    display: flex;
    align-items: center;
    justify-content: center;
    gap: 18px;
  }
  .phone-icon { width: 58px; height: 58px; }
  .phone-number {
    font-family: "Roboto", Arial, sans-serif;
    font-weight: 500;
    font-size: 82px;
    line-height: 1;
    letter-spacing: 1px;
    color: var(--ink);
  }
  .agent-name {
    position: absolute;
    left: 0;
    top: 922px;
    width: 760px;
    text-align: center;
    font-family: "Roboto", Arial, sans-serif;
    font-weight: 500;
    font-size: 79px;
    line-height: 1;
    color: var(--white);
  }
  .agent-web {
    position: absolute;
    left: 0;
    top: 1010px;
    width: 760px;
    text-align: center;
    font-family: "Roboto Condensed", "Arial Narrow", sans-serif;
    font-weight: 300;
    font-size: 52px;
    line-height: 1;
    color: var(--web);
  }
</style>
</head>
<body>
  <main class="yard-sign">
    <div class="house-photo" role="img" aria-label="Dimmed photograph of a two-storey suburban house with lawn and trees"></div>

    <h1 class="headline">FOR SALE</h1>

    <div class="brand">
      <span class="brand-dot"></span>
      <span class="brand-name">Birch Crest, LLC</span>
    </div>

    <div class="phone-bar">
      <svg class="phone-icon" viewBox="0 0 58 58" aria-hidden="true">
        <path d="M10 8c3-3 7-3 9 0l5 8c1.5 2.5 1 5-1 6.5l-3 2.5c2 6 7 12 13 15l2.8-3c1.8-2 4.3-2.2 6.6-.8l7.6 5c2.8 2 2.8 6 0 9-4 4-9 5-15 2C23 47 12 36 7 24 4.5 17 6 12 10 8z" fill="var(--white)"/>
        <path d="M31 14a14 14 0 0 1 13 13" stroke="var(--white)" stroke-width="3" fill="none" stroke-linecap="round"/>
        <path d="M32 6a22 22 0 0 1 20 20" stroke="var(--white)" stroke-width="3" fill="none" stroke-linecap="round"/>
        <path d="M30 22a6 6 0 0 1 6 6" stroke="var(--white)" stroke-width="3" fill="none" stroke-linecap="round"/>
      </svg>
      <span class="phone-number">800-555-0142</span>
    </div>

    <p class="agent-name">JONATHAN DOE</p>
    <p class="agent-web">www.yourwebsite.com</p>
  </main>
</body>
</html>
```